Card design for orthopaedic surgeons working as The Brindlewood Orthopaedic Centre

Business cards, letterhead

Colors

Designer to choose colors to be used in the design.

Requirements
Must have
• Late addition.
• Cards letterhead must have logos of
• Corvane Federated Institute of Surgeons
• Meridale Orthopaedic Society
Nice to have
• Back of card to have space for appointment time to be added by hand and some blank space for writing incidental other notes.

```html
<!DOCTYPE html>
<html lang="en">
<head>
<meta charset="utf-8">
<title>The Brindlewood Orthopaedic Centre – Business Card</title>
<link href="https://fonts.googleapis.com/css2?family=Montserrat:ital,wght@0,400;0,500;0,700;1,700&display=swap" rel="stylesheet">
<style>
  :root {
    --navy: #082c45;
    --sky: #2fa8ee;
    --sky-deep: #1a9ad8;
    --paper: #f1f1f1;
    --paper-shade: #e4e4e4;
    --rule: #a7a9ac;
    --ink: #0b2d48;
    --white: #ffffff;
  }
  * { box-sizing: border-box; margin: 0; padding: 0; }
  html, body {
    width: 1200px; height: 1200px; overflow: hidden;
    background: var(--white);
    font-family: "Montserrat", sans-serif;
    color: var(--ink);
  }
  .card {
    position: absolute; left: 209px; width: 788px; height: 450px;
    overflow: hidden;
    background: linear-gradient(135deg, var(--paper) 0%, #f7f7f7 45%, var(--paper-shade) 100%);
    border: 1px solid #d6d6d6;
  }
  .card--front { top: 105px; }
  .card--back { top: 675px; }
  .card__shapes { position: absolute; inset: 0; width: 100%; height: 100%; }

  /* Front */
  .brand-vertical {
    position: absolute; left: 80px; top: 225px;
    transform: translate(-50%, -50%) rotate(-90deg);
    white-space: nowrap;
    font-size: 20px; font-weight: 400; letter-spacing: 0.2px;
    color: var(--sky);
  }
  .affiliation {
    position: absolute; text-align: center; color: #6d6e71;
  }
  .affiliation__badge { display: block; margin: 0 auto; }
  .affiliation--society { left: 492px; top: 28px; width: 140px; }
  .affiliation__name {
    font-size: 22px; font-weight: 400; letter-spacing: 1px; color: #58595b;
    margin-top: 4px;
  }
  .affiliation__line { font-size: 7.5px; letter-spacing: 0.8px; line-height: 9.5px; }
  .affiliation__line--accent { color: #2b3a8f; }
  .affiliation--institute { left: 620px; top: 30px; width: 156px; }
  .affiliation__caption { font-size: 4.6px; font-weight: 700; margin-top: 4px; color: #3a3a3a; letter-spacing: 0.1px; }

  .doctor {
    position: absolute; right: 71px; top: 207px; text-align: right;
  }
  .doctor__name { font-size: 31px; font-weight: 400; line-height: 38px; }
  .doctor__name strong { font-weight: 700; }
  .doctor__rule { height: 1.5px; background: #6d6e71; width: 250px; margin-left: auto; margin-top: 0; }
  .doctor__degree { font-size: 17.5px; font-weight: 500; margin-top: 4px; }

  .contact {
    position: absolute; right: 65px; text-align: right;
    font-size: 21px; font-weight: 500; white-space: nowrap;
  }
  .contact--phone { top: 287px; right: 71px; }
  .contact--email { top: 340px; }
  .contact--address { top: 394px; }

  .icon { position: absolute; left: 729px; width: 30px; height: 30px; }
  .icon--person { top: 228px; }
  .icon--phone { top: 283px; }
  .icon--mail { top: 337px; }
  .icon--pin { top: 392px; }

  /* Back */
  .brand-line {
    position: absolute; left: 320px; top: 78px; transform: translateX(-50%);
    white-space: nowrap; font-size: 24px; font-weight: 400; color: var(--sky);
  }
  .appointment {
    position: absolute; left: 0; top: 184px; width: 676px; height: 50px;
  }
  .appointment__field {
    position: absolute; inset: 0;
    background: var(--white);
    clip-path: polygon(0 0, 100% 0, 95% 100%, 0 100%);
  }
  .appointment__label {
    position: absolute; left: 0; top: 0; height: 50px; width: 268px;
    background: var(--sky);
    clip-path: polygon(0 0, 250px 0, 268px 100%, 0 100%);
    color: var(--white); font-size: 21px; font-weight: 700; font-style: italic;
    line-height: 50px; padding-left: 44px;
  }
  .note-line {
    position: absolute; left: 50px; width: 383px; height: 3px; background: var(--rule);
  }
  .note-line--first { top: 304px; }
  .note-line--second { top: 385px; }
  .anatomy-visual { position: absolute; inset: 0; }
</style>
</head>
<body>

<section class="card card--front" aria-label="Business card front">
  <svg class="card__shapes" viewBox="0 0 788 450" preserveAspectRatio="none" aria-hidden="true">
    <path fill="var(--sky)" d="M0,0 H198 C120,80 112,215 215,292 C262,340 302,400 342,450 H0 Z"/>
    <path fill="var(--navy)" d="M0,0 H166 C128,70 125,205 215,292 C228,335 212,400 220,450 H0 Z"/>
  </svg>

  <div class="brand-vertical">The Brindlewood Orthopaedic Centre</div>

  <div class="affiliation affiliation--society">
    <svg class="affiliation__badge" width="58" height="58" viewBox="0 0 58 58" role="img" aria-label="Meridale Orthopaedic Society crest">
      <path d="M29 2 L52 12 V30 C52 44 42 52 29 56 C16 52 6 44 6 30 V12 Z" fill="#b89a55"/>
    </svg>
    <div class="affiliation__name">MERIDALE</div>
    <div class="affiliation__line">FELLOW of the</div>
    <div class="affiliation__line">MERIDALE</div>
    <div class="affiliation__line"><span class="affiliation__line--accent">ORTHOPAEDIC</span> SOCIETY</div>
  </div>

  <div class="affiliation affiliation--institute">
    <svg class="affiliation__badge" width="86" height="108" viewBox="0 0 86 108" role="img" aria-label="Corvane Federated Institute of Surgeons crest">
      <path d="M43 4 L78 18 V56 C78 82 62 98 43 104 C24 98 8 82 8 56 V18 Z" fill="#c6553f"/>
    </svg>
    <div class="affiliation__caption">CORVANE FEDERATED INSTITUTE OF SURGEONS</div>
  </div>

  <div class="doctor">
    <div class="doctor__name">Dr. <strong>Lorem</strong> Ipsum</div>
    <div class="doctor__rule"></div>
    <div class="doctor__degree">MS (Ortho), MBBS</div>
  </div>

  <div class="contact contact--phone">+966 44 51290 736</div>
  <div class="contact contact--email">brindlewoodortho@mailbox.com</div>
  <div class="contact contact--address">218 Harlow Crescent, US</div>

  <svg class="icon icon--person" viewBox="0 0 30 30" aria-hidden="true">
    <circle cx="15" cy="15" r="15" fill="var(--navy)"/>
    <circle cx="15" cy="11.5" r="5" fill="var(--white)"/>
    <path d="M6 25 C7 18 23 18 24 25 Z" fill="var(--white)"/>
  </svg>
  <svg class="icon icon--phone" viewBox="0 0 30 30" aria-hidden="true">
    <circle cx="15" cy="15" r="15" fill="var(--navy)"/>
    <rect x="10.5" y="7" width="9" height="16" rx="1.5" fill="none" stroke="var(--white)" stroke-width="1.6"/>
    <circle cx="15" cy="20.3" r="0.9" fill="var(--white)"/>
  </svg>
  <svg class="icon icon--mail" viewBox="0 0 30 30" aria-hidden="true">
    <circle cx="15" cy="15" r="15" fill="var(--navy)"/>
    <rect x="7" y="10" width="16" height="11" fill="none" stroke="var(--white)" stroke-width="1.4"/>
    <path d="M7 10 L15 16.5 L23 10 M7 21 L12.5 15 M23 21 L17.5 15" fill="none" stroke="var(--white)" stroke-width="1.2"/>
  </svg>
  <svg class="icon icon--pin" viewBox="0 0 30 30" aria-hidden="true">
    <circle cx="15" cy="15" r="15" fill="var(--navy)"/>
    <path d="M15 23 C11 18 9.5 15.5 9.5 13 A5.5 5.5 0 0 1 20.5 13 C20.5 15.5 19 18 15 23 Z" fill="var(--white)"/>
    <circle cx="15" cy="13" r="2" fill="var(--navy)"/>
  </svg>
</section>

<section class="card card--back" aria-label="Business card back">
  <svg class="card__shapes" viewBox="0 0 788 450" preserveAspectRatio="none" aria-hidden="true">
    <path fill="var(--sky-deep)" d="M650,0 H700 C730,90 725,190 665,245 C615,295 585,365 572,450 H455 C520,365 598,305 640,235 C675,170 672,75 650,0 Z"/>
  </svg>
  <svg class="anatomy-visual" viewBox="0 0 788 450" preserveAspectRatio="none" role="img" aria-label="Medical imagery of foot, rib cage, spine and hip joints on blue screens">
    <defs>
      <linearGradient id="anatomyTone" x1="0" y1="0" x2="0.4" y2="1">
        <stop offset="0" stop-color="#3d6fa8"/>
        <stop offset="0.45" stop-color="#2a5a9c"/>
        <stop offset="0.7" stop-color="#1d3f86"/>
        <stop offset="1" stop-color="#142a5c"/>
      </linearGradient>
    </defs>
    <path fill="url(#anatomyTone)" d="M655,0 H788 V450 H570 C585,365 615,300 665,248 C725,190 730,90 690,0 Z"/>
  </svg>

  <div class="brand-line">The Brindlewood Orthopaedic Centre</div>

  <div class="appointment">
    <div class="appointment__field"></div>
    <div class="appointment__label">Appointment time</div>
  </div>

  <div class="note-line note-line--first"></div>
  <div class="note-line note-line--second"></div>
</section>

</body>
</html>
```